Main Banner for Hullwrap.com, SIMPLE REDESIGN

We need to redesign the main banner that appears on the homepage of our website.

Attached in the project brief is a reference.

There are alot of things we like that we want to keep from that concept but its overall just something I drew on paint and not designed well.

1. Keep yellow tabs on the right hand side, we want them bigger and bolder and to showcase the bullet points inside.
2. Get rid of the 10 yr warranty emblem and replace that with our Brandell logo also attached to the brief.
3. Keep the bottom header and include hullwrap.com and the phone number, but make it look bolder and nicer.
4. Keep the watermark

Aside from these points what we really need is this but a better cleaner more professional version of it.

Target Market(s)

Visitors to our website hullwrap.com we want this banner to include all the major selling points, branding of the product and info on how to contact us.

Requirements
Must have
• Must be clean and professional. My fear is getting submissions that are too busy or messy. There are a lot of components but the challenge is to put them all in there in a clean professional way.
Should not have
• An image in the background like a beach or some kind of picture want the focus to be the requirements listed in the project description

```html
<!DOCTYPE html>
<html lang="en">
<head>
<meta charset="utf-8">
<title>Brandell Summit Boat Cover – Homepage Banner Options</title>
<link rel="stylesheet" href="https://fonts.googleapis.com/css2?family=Titillium+Web:ital,wght@0,300;0,400;0,700;0,900;1,300;1,400;1,700;1,900&display=swap">
<style>
  :root {
    --page-bg: #e9e6e1;
    --blue-deep: #1569b4;
    --blue-mid: #1f86d0;
    --blue-light: #3aa3e6;
    --light-edge: #d9dadc;
    --light-mid: #f4f4f5;
    --ink-dark: #2b2b2b;
    --ink-mid: #555a60;
    --ink-white: #ffffff;
    --yellow-top: #ffd21a;
    --yellow-bottom: #f7a900;
    --yellow-shade: #c98300;
    --label-ink: #111111;
    --photo-navy: #3a4f9e;
    --photo-grey: #c9cdd3;
  }

  * { box-sizing: border-box; margin: 0; padding: 0; }

  html, body {
    width: 1159px;
    height: 1200px;
    overflow: hidden;
  }

  body {
    position: relative;
    background: var(--page-bg);
    font-family: "Titillium Web", "Arial Narrow", sans-serif;
  }

  /* ---------- Banner ---------- */
  .banner {
    position: absolute;
    left: 62px;
    width: 1013px;
    height: 507px;
    overflow: hidden;
    box-shadow: 0 6px 18px rgba(0,0,0,0.35);
  }
  .banner--blue {
    top: 24px;
    background: radial-gradient(ellipse at 55% 40%, var(--blue-light) 0%, var(--blue-mid) 45%, var(--blue-deep) 100%);
    --title-ink: var(--ink-white);
    --sub-ink: rgba(255,255,255,0.92);
    --mark-tone: rgba(255,255,255,0.10);
  }
  .banner--light {
    top: 614px;
    background: radial-gradient(ellipse at 55% 40%, #ffffff 0%, var(--light-mid) 45%, var(--light-edge) 100%);
    --title-ink: var(--ink-dark);
    --sub-ink: var(--ink-mid);
    --mark-tone: rgba(0,0,0,0.06);
  }

  .banner__mark {
    position: absolute;
    left: 500px;
    top: 30px;
    width: 380px;
    height: 380px;
    border-radius: 50%;
    background: var(--mark-tone);
  }

  /* Heading */
  .banner__brand-square {
    position: absolute;
    left: 160px;
    top: 26px;
    width: 60px;
    height: 60px;
    background: var(--yellow-top);
    border: 3px solid rgba(0,0,0,0.35);
  }
  .banner__title {
    position: absolute;
    left: 234px;
    top: 28px;
    font-size: 41px;
    line-height: 1;
    letter-spacing: 0.5px;
    color: var(--title-ink);
    white-space: nowrap;
    text-transform: uppercase;
  }
  .banner__title-light { font-weight: 300; }
  .banner__title-bold { font-weight: 700; font-style: italic; }

  .banner__stars {
    position: absolute;
    left: 408px;
    top: 88px;
    display: flex;
    gap: 6px;
  }
  .banner__stars svg { width: 34px; height: 34px; }

  /* Product photo area */
  .banner__product {
    position: absolute;
    left: 33px;
    top: 128px;
    width: 480px;
    height: 170px;
    border-radius: 6px;
    background: linear-gradient(160deg, var(--photo-navy) 0%, var(--photo-grey) 100%);
    opacity: 0.85;
  }

  /* Selling point tabs */
  .tab {
    position: absolute;
    right: 0;
    height: 53px;
    display: flex;
    align-items: center;
    padding-left: 44px;
    gap: 10px;
    background: linear-gradient(180deg, var(--yellow-top) 0%, var(--yellow-bottom) 100%);
    clip-path: polygon(0 0, 100% 0, 100% 100%, 14px 100%);
    box-shadow: 0 4px 0 var(--yellow-shade);
    font-size: 27px;
    color: var(--label-ink);
    text-transform: uppercase;
    font-style: italic;
    white-space: nowrap;
  }
  .tab--warranty { top: 152px; width: 355px; }
  .tab--shipping { top: 231px; width: 326px; }
  .tab--waterproof { top: 310px; width: 298px; }
  .tab__icon { width: 24px; height: 24px; flex: none; }
  .tab__light { font-weight: 400; }
  .tab__bold { font-weight: 700; }

  /* Model and price */
  .banner__model {
    position: absolute;
    left: 36px;
    top: 328px;
    font-size: 39px;
    line-height: 1;
    color: var(--title-ink);
    text-transform: uppercase;
    white-space: nowrap;
  }
  .banner__model-light { font-weight: 300; }
  .banner__model-bold { font-weight: 700; font-style: italic; }

  .banner__price-label {
    position: absolute;
    left: 36px;
    top: 393px;
    font-size: 31px;
    line-height: 1;
    color: var(--sub-ink);
    text-transform: uppercase;
    white-space: nowrap;
  }
  .banner__price-label strong { font-weight: 700; font-style: italic; }
  .banner__price-label span { font-weight: 300; }

  .banner__price {
    position: absolute;
    left: 292px;
    top: 385px;
    width: 162px;
    height: 54px;
    display: flex;
    align-items: center;
    justify-content: center;
    background: linear-gradient(180deg, var(--yellow-top), var(--yellow-bottom));
    clip-path: polygon(10px 0, 100% 0, calc(100% - 10px) 100%, 0 100%);
    font-size: 28px;
    font-weight: 700;
    font-style: italic;
    color: var(--label-ink);
  }

  /* Footer band */
  .banner__footer {
    position: absolute;
    left: 0;
    bottom: 0;
    width: 100%;
    height: 47px;
    display: flex;
    align-items: center;
    justify-content: space-between;
    padding: 0 32px 0 34px;
    background: linear-gradient(180deg, var(--yellow-top) 0%, var(--yellow-bottom) 100%);
    border-top: 3px solid rgba(255,255,255,0.45);
    font-size: 23px;
    color: var(--label-ink);
    text-transform: uppercase;
  }
  .footer__item { display: flex; align-items: center; gap: 8px; white-space: nowrap; }
  .footer__item svg { width: 20px; height: 20px; }
  .footer__bold { font-weight: 700; font-style: italic; }
  .footer__light { font-weight: 400; }

  /* Option labels */
  .option-label {
    position: absolute;
    left: 0;
    width: 1159px;
    text-align: center;
    font-size: 34px;
    font-weight: 900;
    color: var(--label-ink);
    text-transform: uppercase;
    letter-spacing: 0.5px;
  }
  .option-label--one { top: 542px; }
  .option-label--two { top: 1136px; }
</style>
</head>
<body>

<section class="banner banner--blue">
  <div class="banner__mark"></div>
  <div class="banner__brand-square"></div>
  <h1 class="banner__title"><span class="banner__title-light">Brandell</span> <span class="banner__title-bold">Summit Boat Cover</span></h1>
  <div class="banner__stars" aria-label="Five star rating">
    <svg viewBox="0 0 24 24"><polygon points="12,1 15,9 23.5,9 16.5,14 19.2,22.5 12,17.3 4.8,22.5 7.5,14 0.5,9 9,9" fill="#ffd21a"/></svg>
    <svg viewBox="0 0 24 24"><polygon points="12,1 15,9 23.5,9 16.5,14 19.2,22.5 12,17.3 4.8,22.5 7.5,14 0.5,9 9,9" fill="#ffd21a"/></svg>
    <svg viewBox="0 0 24 24"><polygon points="12,1 15,9 23.5,9 16.5,14 19.2,22.5 12,17.3 4.8,22.5 7.5,14 0.5,9 9,9" fill="#ffd21a"/></svg>
    <svg viewBox="0 0 24 24"><polygon points="12,1 15,9 23.5,9 16.5,14 19.2,22.5 12,17.3 4.8,22.5 7.5,14 0.5,9 9,9" fill="#ffd21a"/></svg>
    <svg viewBox="0 0 24 24"><polygon points="12,1 15,9 23.5,9 16.5,14 19.2,22.5 12,17.3 4.8,22.5 7.5,14 0.5,9 9,9" fill="#ffd21a"/></svg>
  </div>
  <div class="banner__product" role="img" aria-label="Product photo: boat with a navy fitted cover on a twin-axle trailer"></div>

  <div class="tab tab--warranty">
    <svg class="tab__icon" viewBox="0 0 24 24"><rect x="2" y="4" width="18" height="18" rx="2" fill="none" stroke="#111" stroke-width="2.4"/><path d="M6 12l4 4 12-13" fill="none" stroke="#111" stroke-width="2.6"/></svg>
    <span><span class="tab__light">10 Yr</span> <span class="tab__bold">Warrenty</span></span>
  </div>
  <div class="tab tab--shipping">
    <svg class="tab__icon" viewBox="0 0 24 24"><rect x="2" y="4" width="18" height="18" rx="2" fill="none" stroke="#111" stroke-width="2.4"/><path d="M6 12l4 4 12-13" fill="none" stroke="#111" stroke-width="2.6"/></svg>
    <span><span class="tab__light">Free</span> <span class="tab__bold">Shipping</span></span>
  </div>
  <div class="tab tab--waterproof">
    <svg class="tab__icon" viewBox="0 0 24 24"><rect x="2" y="4" width="18" height="18" rx="2" fill="none" stroke="#111" stroke-width="2.4"/><path d="M6 12l4 4 12-13" fill="none" stroke="#111" stroke-width="2.6"/></svg>
    <span><span class="tab__light">Water</span> <span class="tab__bold">Proof</span></span>
  </div>

  <p class="banner__model"><span class="banner__model-light">Brandell</span> <span class="banner__model-bold">Summit 1200</span></p>
  <p class="banner__price-label"><span>Starting</span> <strong>Price</strong></p>
  <div class="banner__price">$239.99</div>

  <footer class="banner__footer">
    <div class="footer__item">
      <svg viewBox="0 0 20 20"><circle cx="10" cy="10" r="8.5" fill="none" stroke="#111" stroke-width="2"/><ellipse cx="10" cy="10" rx="3.6" ry="8.5" fill="none" stroke="#111" stroke-width="1.6"/><line x1="1.5" y1="10" x2="18.5" y2="10" stroke="#111" stroke-width="1.6"/></svg>
      <span><span class="footer__bold">Hullwrap</span><span class="footer__light">.com</span></span>
    </div>
    <div class="footer__item">
      <svg viewBox="0 0 20 20"><path d="M4 2l3.5 0 1.5 4-2 1.5c1 2.2 2.6 3.8 4.8 4.8L13.3 10l4 1.5V15c0 1.2-1 2-2.2 2C8.5 16.6 3.4 11.5 3 4.9 3 3 3.4 2 4 2z" fill="#111"/></svg>
      <span><span class="footer__bold">Call Us</span> <span class="footer__light">800-555-0147</span></span>
    </div>
  </footer>
</section>

<p class="option-label option-label--one">Design #1</p>

<section class="banner banner--light">
  <div class="banner__mark"></div>
  <div class="banner__brand-square"></div>
  <h1 class="banner__title"><span class="banner__title-light">Brandell</span> <span class="banner__title-bold">Summit Boat Cover</span></h1>
  <div class="banner__stars" aria-label="Five star rating">
    <svg viewBox="0 0 24 24"><polygon points="12,1 15,9 23.5,9 16.5,14 19.2,22.5 12,17.3 4.8,22.5 7.5,14 0.5,9 9,9" fill="#ffc400"/></svg>
    <svg viewBox="0 0 24 24"><polygon points="12,1 15,9 23.5,9 16.5,14 19.2,22.5 12,17.3 4.8,22.5 7.5,14 0.5,9 9,9" fill="#ffc400"/></svg>
    <svg viewBox="0 0 24 24"><polygon points="12,1 15,9 23.5,9 16.5,14 19.2,22.5 12,17.3 4.8,22.5 7.5,14 0.5,9 9,9" fill="#ffc400"/></svg>
    <svg viewBox="0 0 24 24"><polygon points="12,1 15,9 23.5,9 16.5,14 19.2,22.5 12,17.3 4.8,22.5 7.5,14 0.5,9 9,9" fill="#ffc400"/></svg>
    <svg viewBox="0 0 24 24"><polygon points="12,1 15,9 23.5,9 16.5,14 19.2,22.5 12,17.3 4.8,22.5 7.5,14 0.5,9 9,9" fill="#ffc400"/></svg>
  </div>
  <div class="banner__product" role="img" aria-label="Product photo: boat with a navy fitted cover on a twin-axle trailer"></div>

  <div class="tab tab--warranty">
    <svg class="tab__icon" viewBox="0 0 24 24"><rect x="2" y="4" width="18" height="18" rx="2" fill="none" stroke="#111" stroke-width="2.4"/><path d="M6 12l4 4 12-13" fill="none" stroke="#111" stroke-width="2.6"/></svg>
    <span><span class="tab__light">10 Yr</span> <span class="tab__bold">Warrenty</span></span>
  </div>
  <div class="tab tab--shipping">
    <svg class="tab__icon" viewBox="0 0 24 24"><rect x="2" y="4" width="18" height="18" rx="2" fill="none" stroke="#111" stroke-width="2.4"/><path d="M6 12l4 4 12-13" fill="none" stroke="#111" stroke-width="2.6"/></svg>
    <span><span class="tab__light">Free</span> <span class="tab__bold">Shipping</span></span>
  </div>
  <div class="tab tab--waterproof">
    <svg class="tab__icon" viewBox="0 0 24 24"><rect x="2" y="4" width="18" height="18" rx="2" fill="none" stroke="#111" stroke-width="2.4"/><path d="M6 12l4 4 12-13" fill="none" stroke="#111" stroke-width="2.6"/></svg>
    <span><span class="tab__light">Water</span> <span class="tab__bold">Proof</span></span>
  </div>

  <p class="banner__model"><span class="banner__model-light">Brandell</span> <span class="banner__model-bold">Summit 1200</span></p>
  <p class="banner__price-label"><span>Starting</span> <strong>Price</strong></p>
  <div class="banner__price">$239.99</div>

  <footer class="banner__footer">
    <div class="footer__item">
      <svg viewBox="0 0 20 20"><circle cx="10" cy="10" r="8.5" fill="none" stroke="#111" stroke-width="2"/><ellipse cx="10" cy="10" rx="3.6" ry="8.5" fill="none" stroke="#111" stroke-width="1.6"/><line x1="1.5" y1="10" x2="18.5" y2="10" stroke="#111" stroke-width="1.6"/></svg>
      <span><span class="footer__bold">Hullwrap</span><span class="footer__light">.com</span></span>
    </div>
    <div class="footer__item">
      <svg viewBox="0 0 20 20"><path d="M4 2l3.5 0 1.5 4-2 1.5c1 2.2 2.6 3.8 4.8 4.8L13.3 10l4 1.5V15c0 1.2-1 2-2.2 2C8.5 16.6 3.4 11.5 3 4.9 3 3 3.4 2 4 2z" fill="#111"/></svg>
      <span><span class="footer__bold">Call Us</span> <span class="footer__light">800-555-0147</span></span>
    </div>
  </footer>
</section>

<p class="option-label option-label--two">Design #2</p>

</body>
</html>
```